Sleep/Snoring Business - Requires Website - Australia

We are seeking a simple to maintain website for our sleep business. The health care business provides diagnostic and treatment solutions for snoring, sleep disorders and other respiratory problems.

Ideally, colours to match the company logo (attached).

The page must be built using WORDPRESS.

Ideally site will have a home page outlining the business, with 5 sub pages - being "Diagnosis" "Treatment Options", "Prodcuts", "About Us", "Contact Us"

The site home page should include a large picture on the home page.

The "Treatment Options" and "Diagnosis" pages must include:
Allow for a few pictures with assocaited text, plus space for some embeded youtube videos.

"Prodcuts" page should have the ability to show 3-4 products across the page with text below.. that can include external URL to products

The "About Us" page must include:
1. a Map (google map) to identify the various locations. There are 6 in total.
2. A Section to describe our doctors/staff - allow for a picture and some text

The "Contact Us" page must include:
email form
telephone details

The overall design should have a clean and medical/safe feeling

Target Market(s)

People who snore and those with sleeping and respiratory disorders

Industry/Entity Type

Health Care

Coding

Coded - Design and coding required

Number of Pages Required

5+ page

Colors

Designer to choose colors to be used in the design.

Requirements
Must have
• The page must be built using WORDPRESS.
• Ideally site will have a home page outlining the business, with 5 sub pages - being "Diagnosis" "Treatment Options", "Prodcuts", "About Us", "Contact Us"
• The site home page should include a large picture on the home page.
• The "Treatment Options" and "Diagnosis" pages must include:
• Allow for a few pictures with assocaited text, plus space for some embeded youtube videos.
• "Prodcuts" page should have the ability to show 3-4 products across the page with text below.. that can include external URL to products
• The "About Us" page must include:
• 1. a Map (google map) to identify the various locations. There are 6 in total.
• 2. A Section to describe our doctors/staff - allow for a picture and some text
• The "Contact Us" page must include:
• email form
• telephone details
• Pictures must be licenced or free to use
Nice to have
• Home page pictures showing people sleeping well, snoring or fresh air (landscape) type transition pictures (at least 3).
Should not have
• Not to look cheap
• This is a high end healthcare business, so must look that way

```html
<!DOCTYPE html>
<html lang="en">
<head>
<meta charset="utf-8">
<title>Restwell Clinic – Home</title>
<link href="https://fonts.googleapis.com/css2?family=Lato:wght@400;700&family=Oswald:wght@400;500&display=swap" rel="stylesheet">
<style>
  :root {
    --navy: #124a80;
    --sky: #94b1d9;
    --sky-active: #93afd7;
    --white: #ffffff;
    --text-dark: #3a3a3a;
    --hero-light: #d9e27a;
    --hero-mid: #9cc43c;
    --hero-deep: #5f9a22;
  }
  * { margin: 0; padding: 0; box-sizing: border-box; }
  html, body { width: 1200px; height: 859px; overflow: hidden; background: var(--white); }
  body { font-family: 'Lato', sans-serif; position: relative; }

  .site-header { position: absolute; left: 0; top: 0; width: 1200px; height: 117px; background: var(--white); }
  .brand { position: absolute; left: 80px; top: 38px; display: flex; align-items: center; gap: 10px; }
  .brand-dot { width: 18px; height: 18px; border-radius: 50%; background: var(--navy); }
  .brand-name { font-family: 'Lato', sans-serif; font-weight: 700; font-size: 36px; color: var(--navy); letter-spacing: -0.5px; }

  .header-call { position: absolute; left: 922px; top: 36px; display: flex; align-items: center; gap: 4px; }
  .header-call svg { width: 46px; height: 58px; }
  .header-call-label { font-size: 18px; color: var(--navy); line-height: 24px; }
  .header-call-number { font-size: 19px; color: var(--text-dark); line-height: 25px; }

  .main-nav { position: absolute; left: 0; top: 117px; width: 1200px; height: 49px; background: var(--navy); }
  .main-nav ul { list-style: none; position: absolute; left: 80px; top: 0; display: flex; height: 49px; border-right: 1px solid rgba(255,255,255,0.25); }
  .main-nav li { height: 49px; display: flex; align-items: center; justify-content: center; color: var(--white); font-size: 15.5px; text-transform: uppercase; border-left: 1px solid rgba(255,255,255,0.25); }
  .main-nav li:first-child { border-left: none; }
  .main-nav li.is-active { background: var(--sky-active); }

  .hero { position: absolute; left: 0; top: 166px; width: 1200px; height: 525px;
    background:
      radial-gradient(ellipse at 15% 5%, rgba(255,250,200,0.9), rgba(255,250,200,0) 40%),
      linear-gradient(170deg, var(--hero-light) 0%, var(--hero-mid) 45%, var(--hero-deep) 100%); }
  .hero-title { position: absolute; left: 80px; top: 204px; font-family: 'Oswald', sans-serif; font-weight: 400; font-size: 31px; line-height: 37px; color: #111; letter-spacing: -0.3px; }
  .hero-dots { position: absolute; left: 80px; top: 377px; display: flex; gap: 7px; }
  .hero-dots span { width: 13px; height: 13px; border-radius: 50%; background: var(--navy); }
  .hero-dots span.is-current { background: transparent; border: 3px solid var(--navy); box-shadow: inset 0 0 0 2px #cfe0f2; }

  .site-footer { position: absolute; left: 0; top: 691px; width: 1200px; height: 168px; background: var(--sky); color: var(--white); }
  .contact-item { position: absolute; top: 35px; display: flex; gap: 9px; }
  .contact-icon { width: 36px; height: 36px; border-radius: 50%; background: var(--navy); display: flex; align-items: center; justify-content: center; flex: none; }
  .contact-icon svg { width: 16px; height: 16px; }
  .contact-title { font-weight: 700; font-size: 15px; line-height: 18px; margin-top: 2px; }
  .contact-detail { font-size: 14px; line-height: 20px; margin-top: 4px; white-space: nowrap; }
  .footer-brand { position: absolute; left: 1000px; top: 38px; display: flex; align-items: center; gap: 8px; }
  .footer-brand .brand-dot { background: var(--white); width: 14px; height: 14px; }
  .footer-brand .brand-name { color: var(--white); font-size: 27px; }
  .footer-rule { position: absolute; left: 79px; top: 113px; width: 1041px; height: 1px; background: rgba(255,255,255,0.55); }
  .copyright { position: absolute; left: 82px; top: 129px; font-size: 13.5px; }
  .social-links { position: absolute; left: 962px; top: 123px; display: flex; gap: 10px; }
  .social-links span { width: 32px; height: 32px; border-radius: 50%; background: var(--white); }
</style>
</head>
<body>
  <header class="site-header">
    <div class="brand"><span class="brand-dot"></span><span class="brand-name">Restwell</span></div>
    <div class="header-call">
      <svg viewBox="0 0 48 56" aria-hidden="true">
        <path d="M30 4 A24 24 0 0 0 30 52" fill="none" stroke="#94b1d9" stroke-width="3"/>
        <path d="M22 14 q-6 2 -5 14 q2 12 9 16 l4 -2 q1 -1 0 -3 l-4 -6 q-1 -1 -3 0 l-2 1 q-3 -6 -2 -12 l2 -1 q2 -1 1 -3 l-1 -7 q0 -2 -2 -2z" fill="#94b1d9"/>
        <line x1="38" y1="2" x2="38" y2="54" stroke="#e1e1e1" stroke-width="1"/>
      </svg>
      <div>
        <div class="header-call-label">CALL US:</div>
        <div class="header-call-number">555.018.2046</div>
      </div>
    </div>
  </header>

  <nav class="main-nav">
    <ul>
      <li class="is-active" style="width:132px">Home</li>
      <li style="width:166px">Diagnosis</li>
      <li style="width:239px">Treatment Options</li>
      <li style="width:161px">Products</li>
      <li style="width:161px">About Us</li>
      <li style="width:181px">Contact Us</li>
    </ul>
  </nav>

  <section class="hero" role="img" aria-label="Woman with arms outstretched breathing fresh air in a sunny field of tall green grass">
    <h1 class="hero-title">We Provide Diagnostic And Treatment<br>Solutions For Snoring, Sleep Disorders<br>And Other Respiratory Problems</h1>
    <div class="hero-dots"><span class="is-current"></span><span></span><span></span><span></span></div>
  </section>

  <footer class="site-footer">
    <div class="contact-item" style="left:81px">
      <div class="contact-icon"><svg viewBox="0 0 16 16"><path d="M8 1a5 5 0 0 0-5 5c0 4 5 9 5 9s5-5 5-9a5 5 0 0 0-5-5z" fill="#fff"/><circle cx="8" cy="6" r="1.8" fill="#124a80"/></svg></div>
      <div><div class="contact-title">Restwell Clinic</div><div class="contact-detail">48, Harbour Lane, Northbridge - 204716</div></div>
    </div>
    <div class="contact-item" style="left:473px">
      <div class="contact-icon"><svg viewBox="0 0 16 16"><path d="M4 2 l2.5 0 l1 3.5 l-1.5 1.2 q1 2.5 3.3 3.3 l1.2-1.5 l3.5 1 l0 2.5 q-1 1.5 -3 1 q-6-2 -8-8 q-0.5-2 1-3z" fill="#fff"/></svg></div>
      <div><div class="contact-title">Call Us :</div><div class="contact-detail">555.018.2046</div></div>
    </div>
    <div class="contact-item" style="left:703px">
      <div class="contact-icon"><svg viewBox="0 0 16 16"><rect x="2" y="4" width="12" height="8" fill="#fff"/><path d="M2 4 l6 5 l6-5" fill="none" stroke="#124a80" stroke-width="1.2"/></svg></div>
      <div><div class="contact-title">Email Us :</div><div class="contact-detail">info@restwellclinic.com</div></div>
    </div>
    <div class="footer-brand"><span class="brand-dot"></span><span class="brand-name">Restwell</span></div>
    <div class="footer-rule"></div>
    <p class="copyright">Copyright © 2017 Restwell Clinic. All Rights Reserved.</p>
    <div class="social-links" aria-label="Social links"><span></span><span></span><span></span><span></span></div>
  </footer>
</body>
</html>
```